Stonevale Business Card Design

The Stonevale Co is an aggregate (crushing) equipment dealer serving Western Canadian provinces. Stonevale is a distributor of aggregate equipment for different manufacturers.

We are looking to change and update the existing business card which has been used since the existence of the company. A copy of existing card has been attached for reference. The Stonevale Co logo we want to remain the same and we want the green color to remain the same.

We are wanting something new with a different look. A refreshing card to show a new modern and updated look. No longer wanting to have the manufacturers on the back of the card but something more like our logo on the back of the card with a statement like "Crushing Solutions"

ideas could be:
- card can be different colors on front and back
- front or reverse of the card could possibly be the green color with the logo in black

Target Market(s)

Owners of Aggregate/Crushing companies

Contact Information for Business Card

see above

Requirements
Must have
• - logo to remain same along with same font within logo
• - green color to remain same
Nice to have
• as noted above under project description
Should not have

```html
<!DOCTYPE html>
<html lang="en">
<head>
<meta charset="utf-8">
<title>The Stonevale Co – Business Card</title>
<link href="https://fonts.googleapis.com/css2?family=Archivo+Black&family=Montserrat:wght@300;400;600&family=Raleway:wght@300&display=swap" rel="stylesheet">
<style>
  :root {
    --olive: #8f8c37;
    --ink: #231f20;
    --paper: #ffffff;
    --backdrop: #e9ebeb;
  }
  * { margin: 0; padding: 0; box-sizing: border-box; }
  html, body { width: 1200px; height: 1000px; overflow: hidden; }
  body { background: var(--backdrop); position: relative; font-family: "Montserrat", sans-serif; }

  .card { position: absolute; width: 700px; height: 400px; overflow: hidden; box-shadow: 0 6px 18px rgba(0,0,0,.12); }

  /* Back of card */
  .card-back { left: 250px; top: 70px; background: var(--olive); }
  .card-back .frame { position: absolute; left: 40px; top: 36px; right: 40px; bottom: 36px; border: 2px solid var(--ink); }
  .card-back .wordmark {
    position: absolute; left: 0; right: 0; top: 130px;
    display: flex; align-items: center; justify-content: center; gap: 18px;
    font-family: "Archivo Black", sans-serif; font-size: 44px; color: var(--ink); letter-spacing: 1px;
  }
  .card-back .wordmark .dot { width: 30px; height: 30px; border-radius: 50%; background: var(--ink); }
  .card-back .tagline {
    position: absolute; left: 0; right: 0; bottom: 22px; text-align: center;
  }
  .card-back .tagline span {
    background: var(--olive); padding: 0 18px;
    font-family: "Raleway", sans-serif; font-weight: 300; font-size: 24px; letter-spacing: 2px; color: var(--ink);
  }

  /* Front of card */
  .card-front { left: 250px; top: 530px; background: var(--olive); color: var(--paper); }
  .card-front .shapes { position: absolute; inset: 0; }
  .card-front .brand {
    position: absolute; right: 30px; top: 52px;
    display: flex; align-items: center; gap: 10px;
    font-family: "Archivo Black", sans-serif; font-size: 22px; letter-spacing: .5px;
  }
  .card-front .brand .dot { width: 16px; height: 16px; border-radius: 50%; background: var(--paper); }
  .card-front .name { position: absolute; left: 40px; top: 160px; font-size: 30px; font-weight: 600; letter-spacing: 1px; }
  .contact-list { position: absolute; list-style: none; }
  .contact-list li { display: flex; align-items: center; gap: 16px; font-weight: 400; }
  .contact-list svg { width: 18px; height: 18px; fill: var(--paper); flex: none; }
  .phones { left: 42px; top: 232px; }
  .phones li { font-size: 24px; height: 31px; letter-spacing: 1px; }
  .online { left: 420px; top: 138px; }
  .online li { font-size: 22px; height: 36px; }
  .card-front .address { position: absolute; left: 300px; width: 370px; top: 300px; text-align: center; font-size: 14px; letter-spacing: .5px; }
  .card-front .services { position: absolute; left: 0; right: 0; top: 350px; text-align: center; font-size: 22px; font-weight: 300; letter-spacing: 1px; }
  .card-front .services .sep { margin: 0 10px; }
</style>
</head>
<body>

<section class="card card-back" aria-label="Card back">
  <div class="frame"></div>
  <div class="wordmark"><span class="dot"></span>THE STONEVALE CO.</div>
  <div class="tagline"><span>CRUSHING SOLUTIONS</span></div>
</section>

<section class="card card-front" aria-label="Card front">
  <svg class="shapes" viewBox="0 0 700 400" width="700" height="400">
    <path d="M0 0 H700 V118 H430 Q415 118 412 132 L400 212 H0 Z" fill="#231f20"/>
    <line x1="400" y1="212" x2="700" y2="212" stroke="#231f20" stroke-width="2"/>
    <path d="M300 290 H660 V322 Q660 342 640 342 H320 Q300 342 300 322 Z" fill="#231f20"/>
    <line x1="0" y1="342" x2="700" y2="342" stroke="#231f20" stroke-width="2"/>
  </svg>

  <div class="brand"><span class="dot"></span>THE STONEVALE CO.</div>
  <div class="name">DALE MORROW</div>

  <ul class="contact-list online">
    <li><svg viewBox="0 0 24 24"><path d="M2 5h20v14H2z M2 5l10 8 10-8" fill="#fff"/><path d="M2 5l10 8 10-8" fill="none" stroke="#8f8c37" stroke-width="2"/></svg>dale@stonevale.com</li>
    <li><svg viewBox="0 0 24 24"><circle cx="12" cy="12" r="10" fill="none" stroke="#fff" stroke-width="2"/><ellipse cx="12" cy="12" rx="4.5" ry="10" fill="none" stroke="#fff" stroke-width="2"/><path d="M2 12h20M4 7h16M4 17h16" stroke="#fff" stroke-width="1.6"/></svg>www.stonevale.ca</li>
  </ul>

  <ul class="contact-list phones">
    <li><svg viewBox="0 0 24 24"><path d="M3 8q9-6 18 0v3h-5V9q-3-1-6 0v2H3z"/><rect x="5" y="12" width="14" height="9" rx="2"/></svg>555 . 210 . 4471</li>
    <li><svg viewBox="0 0 24 24"><path d="M6 2l4 5-2 3q2 4 6 6l3-2 5 4-3 4Q9 22 2 6z"/></svg>555 . 318 . 9062</li>
    <li><svg viewBox="0 0 24 24"><rect x="6" y="2" width="12" height="6"/><rect x="2" y="9" width="20" height="9" rx="2"/><rect x="6" y="15" width="12" height="7"/></svg>555 . 746 . 2385</li>
  </ul>

  <div class="address">2218-48B AVENUE, HARLOW, ALBERTA T0X 3K1</div>
  <div class="services">SCREENERS<span class="sep">|</span>CRUSHERS<span class="sep">|</span>STACKERS</div>
</section>

</body>
</html>
```